Wordpress design for company website

We need a Wordpress design for a new brand of payment service called 804. Please see 2 mockup pages attached as guidance.
Updates

Reason: Hi all, we're extending the deadline for this design project by 7 days to have more time for more design submissions to come in.

Thank you.

Target Market(s)

Consumers in Southeast Asia with no credit cards

Industry/Entity Type

It Company

Requirements
Should not have
• Too much color

```html
<!DOCTYPE html>
<html lang="en">
<head>
<meta charset="utf-8">
<title>804 — Payment Service</title>
<link rel="stylesheet" href="https://fonts.googleapis.com/css2?family=Arimo:wght@400;700&display=swap">
<style>
:root{
  --bg:#efefef;
  --page:#ffffff;
  --ink:#444444;
  --ink-soft:#666666;
  --ink-light:#8a8a8a;
  --line:#d2d2d2;
  --sky:#8dd0f2;
  --blue:#1ba8e0;
  --navy:#1b5aa2;
  --deep:#1a4a8c;
  --green:#2fa84a;
  --link:#1a9ad6;
}
*{margin:0;padding:0;box-sizing:border-box}
html,body{width:1200px;height:751px;overflow:hidden;background:var(--bg);font-family:"Arimo",Arial,sans-serif;color:var(--ink)}
.page{position:absolute;left:256px;top:0;width:690px;height:751px;background:var(--page)}
.abs{position:absolute}
.account-links{left:767px;top:84px;font-size:9px;color:var(--ink-soft)}
.brand{left:312px;top:104px;display:flex;align-items:center;gap:6px;color:var(--green);font-weight:700;font-size:32px;letter-spacing:1px}
.brand .mark{width:16px;height:16px;background:var(--green);border-radius:50%}
.btn{position:absolute;display:flex;align-items:center;justify-content:center;color:#fff;font-size:9px;font-weight:400}
.btn.sky{background:var(--sky)}
.btn.blue{background:var(--blue)}
.btn.navy{background:var(--navy)}
.btn.deep{background:var(--deep);font-weight:700}
.side-tab{left:918px;top:200px;width:23px;height:62px;background:var(--navy);color:#fff;font-size:9px;font-weight:700;display:flex;align-items:center;justify-content:center;box-shadow:0 0 3px rgba(0,0,0,.3)}
.side-tab span{transform:rotate(-90deg);white-space:nowrap}
.hero{left:293px;top:158px;width:602px;height:163px;border:1px solid var(--line);border-radius:6px}
.hero h1{position:absolute;left:33px;top:16px;width:255px;white-space:nowrap;font-size:12px;letter-spacing:-0.3px;font-weight:700;color:var(--ink)}
.hero p{position:absolute;left:33px;top:38px;width:228px;font-size:8.3px;line-height:12px;color:var(--ink-soft)}
.hero-photo{left:595px;top:172px;width:285px;height:137px;border-radius:6px;z-index:1;background:linear-gradient(120deg,#d9dde0 0%,#8a9aa6 40%,#c4ccd2 70%,#eef0f2 100%);box-shadow:0 1px 3px rgba(0,0,0,.3)}
.card{position:absolute;top:342px;height:105px;overflow:hidden}
.card .tab{position:absolute;left:0;top:5px;height:22px;padding:0 10px 0 12px;background:rgba(255,255,255,.92);font-size:12.5px;color:var(--ink);display:flex;align-items:center}
.card-merchants{left:294px;width:178px;background:linear-gradient(135deg,#f2d6e4 0%,#e9e4ee 45%,#f6e8d8 100%)}
.card-locations{left:504px;width:180px;background:linear-gradient(110deg,#9cd96a 0%,#58b63a 45%,#e6e6e6 62%,#f2f2f2 100%)}
.card-signup{left:715px;width:180px;background:linear-gradient(120deg,#c9c9c9 0%,#e4e4e4 40%,#f2f2f2 100%)}
.merchant-logo{left:320px;top:377px;width:125px;height:29px;background:var(--deep);color:#fff;font-size:17px;font-weight:700;display:flex;align-items:center;justify-content:center}
.arrow{top:377px;width:7px;height:29px;background:#b9b9b9}
.stat{right:0;width:90px;text-align:right;color:var(--ink-light)}
.col{position:absolute;top:472px;width:289px}
.col h2{font-size:10.5px;font-weight:700;color:var(--ink);margin-bottom:4px}
.col p{font-size:8.3px;line-height:11px;color:var(--ink-soft);text-align:justify}
.col a{display:block;text-align:right;color:var(--link);font-size:8.5px;margin-top:8px;text-decoration:underline}
.footer{left:293px;top:580px;width:602px;height:112px;border:1px solid var(--line);border-radius:6px}
.fcol{position:absolute;top:14px}
.fcol h3{font-size:8.5px;font-weight:700;color:var(--ink-soft);margin-bottom:9px}
.fcol ul{list-style:none;font-size:6px;line-height:8px;color:var(--ink-light)}
.fcol .pair{display:flex;gap:28px}
.divider{position:absolute;top:17px;width:1px;height:68px;background:var(--line)}
.social{display:flex;gap:3px;margin-top:6px}
.social i{width:13px;height:13px;background:var(--navy);border-radius:2px}
.legal{position:absolute;left:0;right:0;top:91px;text-align:center;font-size:5.5px;color:var(--ink-light)}
.copyright{left:294px;top:697px;width:601px;height:18px;background:var(--blue);color:#fff;font-size:6.5px;font-weight:700;display:flex;align-items:center;justify-content:center}
</style>
</head>
<body>
<div class="page"></div>

<div class="abs account-links">View my transactions &nbsp;|&nbsp; Sign In</div>
<div class="abs brand"><span class="mark"></span>804</div>

<div class="btn sky" style="left:667px;top:110px;width:102px;height:31px">What is 804?</div>
<div class="btn blue" style="left:784px;top:110px;width:111px;height:31px">Use 804 for my Biz</div>
<div class="btn navy" style="left:908px;top:110px;width:33px;height:31px;font-weight:700">FAQ</div>
<div class="abs side-tab"><span>Friendlane</span></div>

<section class="abs hero">
  <h1>How do I use 804 service with my business?</h1>
  <p>Lorem Ipsum is simply dummy text of the printing and typesetting industry. Lorem Ipsum has been the industry's standard dummy text ever since the 1500s, when an unknown printer took a galley of type and scrambled it to make a type specimen book. It has survived not only five centuries, but also the leap into electronic typesetting, remaining essentially</p>
</section>
<div class="btn sky" style="left:325px;top:275px;width:102px;height:31px">What is 804?</div>
<div class="abs hero-photo" role="img" aria-label="Photo of three colleagues working together at a laptop"></div>

<div class="card card-merchants" role="img" aria-label="Colourful swirl background">
  <div class="tab">804 Merchants</div>
</div>
<div class="abs arrow" style="left:312px"></div>
<div class="abs arrow" style="left:447px"></div>
<div class="abs merchant-logo">Friendlane</div>
<div class="btn sky" style="left:389px;top:415px;width:72px;height:22px;font-size:9.5px;font-weight:700">Read More</div>

<div class="card card-locations" role="img" aria-label="Green globe illustration">
  <div class="tab">Locations</div>
  <div class="abs stat" style="top:25px;font-size:8.5px;right:10px">More than</div>
  <div class="abs stat" style="top:36px;font-size:16px;right:10px;color:#777">12000</div>
  <div class="abs stat" style="top:54px;font-size:8.5px;right:10px">payment locations.</div>
</div>
<div class="btn blue" style="left:572px;top:415px;width:102px;height:22px;font-size:9.5px;font-weight:700">Show Locations</div>

<div class="card card-signup" role="img" aria-label="Illustration of a running figure carrying a parcel">
  <div class="tab">Sign Up</div>
  <div class="abs" style="right:14px;top:8px;color:var(--green);font-weight:700;font-size:14px">804</div>
  <div class="abs" style="right:13px;top:34px;width:120px;text-align:right;font-size:8.3px;line-height:11px;color:var(--ink-soft)">Are you interested in 804<br>as a payment option<br>for your business?</div>
</div>
<div class="btn deep" style="left:781px;top:415px;width:102px;height:22px">Become 804 Merchant</div>

<div class="col" style="left:294px">
  <h2>Show what makes 804 special</h2>
  <p>There are many variations of passages of Lorem Ipsum available, but the majority have suffered alteration in some form, by injected humour, or randomised words which don't look even slightly believable. If you are going to use a passage of Lorem Ipsum, you need to be sure there isn't anything embarrassing hidden in the middle of text.</p>
  <a>Learn more about 804</a>
</div>
<div class="col" style="left:608px;width:287px">
  <h2>How to integrate 804?</h2>
  <p>It is a long established fact that a reader will be distracted by the readable content of a page when looking at its layout. The point of using Lorem Ipsum is that it has a more-or-less normal distribution of letters, as opposed to using 'Content here, content here', making it look like readable English.</p>
  <a style="margin-top:19px">See many steps of 804 integration</a>
</div>

<footer class="abs footer">
  <div class="fcol" style="left:39px">
    <h3>Choose your Region</h3>
    <div class="pair">
      <ul><li>Thailand</li><li>Pilipinne</li><li>Vietnam</li></ul>
      <ul><li>Malaysia</li><li>Singapore</li><li>Cambodia</li></ul>
    </div>
  </div>
  <div class="divider" style="left:164px"></div>
  <div class="fcol" style="left:194px">
    <h3>Partners/ Merchants</h3>
    <div class="pair" style="gap:34px">
      <ul><li>Become a partner</li><li>Education</li><li>Non-Profits</li></ul>
      <ul><li>Reseller</li><li>Affiliates</li></ul>
    </div>
  </div>
  <div class="divider" style="left:336px"></div>
  <div class="fcol" style="left:363px">
    <h3>Need Help?</h3>
    <ul><li>Customer Support</li><li>Live Chat Support</li><li>Track a transaction</li></ul>
  </div>
  <div class="divider" style="left:448px"></div>
  <div class="fcol" style="left:475px">
    <h3>Join Our Community</h3>
    <div style="font-size:7.5px;color:var(--link);text-decoration:underline">Newsletter Sing up</div>
    <div style="font-size:7.5px;font-weight:700;color:var(--ink-soft);margin-top:6px">Become a fan</div>
    <div class="social"><i></i><i></i><i></i><i></i></div>
  </div>
  <div class="legal">Press Releases &nbsp;|&nbsp; Privacy Statement &nbsp;|&nbsp; Terms of Use &nbsp;|&nbsp; Jobs &nbsp;|&nbsp; Sitemap &nbsp;|&nbsp; Tell us what you think</div>
</footer>
<div class="abs copyright">Copyright © 2010 Shop Nova Co. Ltd</div>
</body>
</html>
```